Steel Company / Iron Railing Business Card Template

We are a custom steel fabrication company located in Trainer, PA. In business since 1979, we recently developed a new logo, and we're looking for a business card design to help display the new logo and our business. The name of the company is Kelvane Metalcraft. The Office Phone number is (610) 555-0143. We fabricate and install custom "wrought iron" railings on our residential side, we also fabricate and erect structural steel (think cranes and steel beams in buildings) on our commercial side. Looking to get a business card template designed. Something modern, but professional. Clear and easy to read. Front should have all business and employee information including phone number(s), email address, business information, etc. back should spotlight logo.

Industry/Entity Type

Construction / Home Improvement

Contact Information for Business Card

Business information is Kelvane Metalcraft, 48 Dunmore Blvd Suite 3307, Trainer, PA 19058. Phone number is (610) 555-0143. Website is www.kelvanemetal.example Business card should be for "Paul Hendry" with the job title "Sales & Estimating" but be editable for other employees. Paul's phone number is (610) 555-0178

Colors

Designer to choose colors to be used in the design.

Requirements
Must have
• Modern Feel, Design should be sized for standard business card sizing 3.5" x 2" (88.9mm x 50.8mm)

```html
<!DOCTYPE html>
<html lang="en">
<head>
<meta charset="utf-8">
<title>Kelvane Metalcraft – Business Card</title>
<link rel="stylesheet" href="https://fonts.googleapis.com/css2?family=Figtree:wght@400;500;700&display=swap">
<style>
  :root {
    --navy: #1f3a80;
    --navy-deep: #1c3575;
    --red: #c8202c;
    --ink: #1d1d24;
    --card-white: #f3f3f3;
    --stair-tint: #f1d9d9;
    --service-text: #c9cfdf;
    --page: #e4e6e5;
  }
  * { box-sizing: border-box; margin: 0; padding: 0; }
  html, body { width: 1200px; height: 1200px; overflow: hidden; }
  body {
    background: var(--page);
    font-family: "Figtree", "Helvetica Neue", Arial, sans-serif;
    display: flex; flex-direction: column; align-items: center; justify-content: center;
    gap: 44px;
  }
  .card {
    position: relative; width: 900px; height: 514px;
    border-radius: 4px; overflow: hidden;
    box-shadow: 0 10px 28px rgba(0,0,0,.18);
  }
  .card-front { background: var(--card-white); color: var(--ink); }
  .stair-decor {
    position: absolute; left: 320px; top: 0; width: 560px; height: 514px;
    background: radial-gradient(ellipse at 55% 45%, var(--stair-tint) 0%, rgba(241,217,217,.55) 45%, rgba(241,217,217,0) 72%);
  }
  .front-info { position: absolute; left: 85px; top: 60px; }
  .person-name { font-size: 34px; font-weight: 700; color: var(--navy); line-height: 1.1; }
  .person-title { font-size: 23px; font-weight: 400; margin-top: 4px; }
  .company-name { font-size: 23px; font-weight: 700; color: var(--red); margin-top: 74px; letter-spacing: .2px; }
  .address { font-size: 23px; line-height: 32px; margin-top: 8px; }
  .contact-list { list-style: none; margin-top: 22px; }
  .contact-list li { display: flex; align-items: center; gap: 12px; font-size: 23px; line-height: 32px; }
  .contact-list svg { width: 20px; height: 20px; fill: var(--navy); flex: none; }
  .front-mark {
    position: absolute; left: 560px; top: 300px; width: 260px;
    display: flex; align-items: center; justify-content: center; gap: 10px;
  }
  .mark-dot { width: 16px; height: 16px; border-radius: 50%; background: var(--red); flex: none; }
  .mark-name { font-size: 30px; font-weight: 700; color: var(--navy); line-height: 1.1; text-align: center; }
  .card-back { background: var(--navy-deep); color: #fff; text-align: center; }
  .back-mark {
    position: absolute; left: 0; right: 0; top: 130px;
    display: flex; align-items: center; justify-content: center; gap: 14px;
  }
  .back-mark .mark-name { color: #fff; font-size: 46px; }
  .back-mark .mark-dot { width: 22px; height: 22px; }
  .services-heading {
    position: absolute; left: 0; right: 0; top: 328px;
    font-size: 23px; font-weight: 700; color: var(--service-text);
  }
  .services-heading span { display: inline-block; padding-bottom: 8px; border-bottom: 3px solid var(--service-text); }
  .services-list { position: absolute; left: 0; right: 0; top: 383px; }
  .services-row { display: flex; justify-content: center; gap: 18px; font-size: 21px; line-height: 29px; color: var(--service-text); }
  .services-row span::before {
    content: ""; display: inline-block; width: 9px; height: 9px; border-radius: 50%;
    background: var(--red); margin-right: 10px; vertical-align: middle; position: relative; top: -2px;
  }
</style>
</head>
<body>
  <section class="card card-front">
    <div class="stair-decor" role="img" aria-label="Faint spiral staircase illustration"></div>
    <div class="front-info">
      <h1 class="person-name">Paul Hendry</h1>
      <p class="person-title">Sales &amp; Estimating</p>
      <p class="company-name">KELVANE METALCRAFT</p>
      <p class="address">48 Dunmore Blvd Suite 3307,<br>Trainer, PA 19058</p>
      <ul class="contact-list">
        <li><svg viewBox="0 0 24 24" aria-hidden="true"><path d="M6.6 10.8a15.1 15.1 0 0 0 6.6 6.6l2.2-2.2c.3-.3.7-.4 1-.2 1.1.4 2.3.6 3.6.6.6 0 1 .4 1 1V20c0 .6-.4 1-1 1A17 17 0 0 1 3 4c0-.6.4-1 1-1h3.5c.6 0 1 .4 1 1 0 1.3.2 2.5.6 3.6.1.3 0 .7-.2 1z"/></svg>(610) 555-0143</li>
        <li><svg viewBox="0 0 24 24" aria-hidden="true"><path d="M7 1h10a2 2 0 0 1 2 2v18a2 2 0 0 1-2 2H7a2 2 0 0 1-2-2V3a2 2 0 0 1 2-2zm0 3v14h10V4zm5 15.5a1.2 1.2 0 1 0 0 2.4 1.2 1.2 0 0 0 0-2.4z"/></svg>(610) 555-0178</li>
        <li><svg viewBox="0 0 24 24" aria-hidden="true"><path d="M2 5h20v14H2zm2 2v.5l8 5.5 8-5.5V7l-8 5.2z"/></svg>info@kelvanemetal.example</li>
        <li><svg viewBox="0 0 24 24" aria-hidden="true"><path d="M12 2a10 10 0 1 0 0 20 10 10 0 0 0 0-20zm6.9 9h-3a15 15 0 0 0-1.4-6.4A8 8 0 0 1 18.9 11zM12 4c1 1.4 1.8 4 1.9 7h-3.8C10.2 8 11 5.4 12 4zM9.5 4.6A15 15 0 0 0 8.1 11h-3a8 8 0 0 1 4.4-6.4zM5.1 13h3a15 15 0 0 0 1.4 6.4A8 8 0 0 1 5.1 13zm6.9 7c-1-1.4-1.8-4-1.9-7h3.8c-.1 3-.9 5.6-1.9 7zm2.5-.6a15 15 0 0 0 1.4-6.4h3a8 8 0 0 1-4.4 6.4z"/></svg>www.kelvanemetal.example</li>
      </ul>
    </div>
    <div class="front-mark">
      <span class="mark-dot"></span>
      <span class="mark-name">Kelvane Metalcraft</span>
    </div>
  </section>

  <section class="card card-back">
    <div class="back-mark">
      <span class="mark-dot"></span>
      <span class="mark-name">Kelvane Metalcraft</span>
    </div>
    <h2 class="services-heading"><span>Our Services</span></h2>
    <div class="services-list">
      <p class="services-row"><span>wrought iron railings</span><span>structural steel</span><span>steel stairs &amp; decks</span><span>iron &amp; steel gates</span></p>
      <p class="services-row"><span>steel fire escapes &amp; balconies</span><span>plasma cutting</span><span>window guards</span><span>steel stairs</span></p>
      <p class="services-row"><span>balcony rails</span></p>
    </div>
  </section>
</body>
</html>
```